BRTW Traditional Business Card Project

Please see attached....just a simple business card... on attachment- please use the exact font, style, etc as the attached "Dal Rupert Huxley" card... however, replace with the "Owen Bartholomew Lindqvist" text and address below the card.

```html
<!DOCTYPE html>
<html lang="en">
<head>
<meta charset="utf-8">
<title>BRTW Business Card</title>
<link href="https://fonts.googleapis.com/css2?family=Tinos:wght@700&family=Michroma&family=Questrial&display=swap" rel="stylesheet">
<style>
  :root {
    --backdrop: #7a4418;
    --card: #ffffff;
    --ink: #111111;
    --shadow: rgba(0, 0, 0, 0.45);
  }
  * { margin: 0; padding: 0; box-sizing: border-box; }
  html, body { width: 1200px; height: 900px; overflow: hidden; }
  body { background: var(--backdrop); position: relative; color: var(--ink); }

  .card {
    position: absolute;
    left: 303px;
    width: 559px;
    height: 342px;
    background: var(--card);
    box-shadow: 3px 4px 6px var(--shadow);
  }
  .card--front { top: 127px; }
  .card--back { top: 493px; }

  .serif-caps {
    font-family: "Tinos", "Times New Roman", serif;
    font-weight: 700;
    font-variant: small-caps;
    white-space: nowrap;
    position: absolute;
    line-height: 1;
  }
  .wide-caps {
    font-family: "Michroma", sans-serif;
    text-transform: uppercase;
    white-space: nowrap;
    position: absolute;
    line-height: 1;
  }
  .contact {
    font-family: "Questrial", sans-serif;
    position: absolute;
    line-height: 1;
    white-space: nowrap;
  }

  /* front */
  .firm-name--small { left: 29px; top: 31px; font-size: 21px; }
  .firm-tag--small { left: 41px; top: 58px; font-size: 9.5px; letter-spacing: 1.6px; }

  .person-name { left: 0; width: 100%; text-align: center; top: 135px; font-size: 29px; }
  .person-title { left: 0; width: 100%; text-align: center; top: 171px; font-size: 12px; letter-spacing: 2.6px; padding-left: 4px; }

  .address { left: 28px; top: 256px; font-size: 13.5px; }
  .address span { display: block; margin-bottom: 5px; }
  .address .web { font-size: 15px; }

  .reach { right: 28px; top: 253px; font-size: 15.5px; text-align: right; }
  .reach span { display: block; margin-bottom: 4.5px; }

  /* back */
  .firm-name--large { left: 0; width: 100%; text-align: center; top: 137px; font-size: 31px; }
  .firm-tag--large { left: 0; width: 100%; text-align: center; top: 182px; font-size: 14px; letter-spacing: 3px; padding-left: 3px; }
</style>
</head>
<body>
  <section class="card card--front" aria-label="Business card front">
    <div class="serif-caps firm-name--small">Bay Region</div>
    <div class="wide-caps firm-tag--small">Trial Works Group, PLC</div>

    <div class="serif-caps person-name">Owen Bartholomew Lindqvist</div>
    <div class="wide-caps person-title">Attorney at Law</div>

    <div class="contact address">
      <span>2140 CEDAR LANE, SUITE B</span>
      <span>MAPLE RIDGE, CA 90210</span>
      <span class="web">www.lawbrtw.com</span>
    </div>

    <div class="contact reach">
      <span>TEL:(555) 214-7300</span>
      <span>FAX:(555) 214-7301</span>
      <span>olindqvist@lawbrtw.com</span>
    </div>
  </section>

  <section class="card card--back" aria-label="Business card back">
    <div class="serif-caps firm-name--large">Bay Region</div>
    <div class="wide-caps firm-tag--large">Trial Works Group, PLC</div>
  </section>
</body>
</html>
```